Loom Harbor commercial brochure

We need a brochure that presents our services for commercial use. Without going into the details of our offers, that the prospect understands our added value and our expertise for the creation of a showcase site, e-commerce site and personalized, tailor-made application.

Please respect the graphic charter

Target Market(s)

Small and medium enterprises

Colors
F0912C
F2A743
F7CA91
FBE8D2
FDF5EE

Requirements
Must have
• a good presentation of our offers on several different pages
Nice to have
• little text but a lot of clarity and precision in the information
Should not have
• too much information, heavy design

```html
<!DOCTYPE html>
<html lang="fr">
<head>
<meta charset="utf-8">
<title>Loom Harbor – Brochure</title>
<link href="https://fonts.googleapis.com/css2?family=Quicksand:wght@400;500;600;700&family=PT+Sans&display=swap" rel="stylesheet">
<style>
  :root{
    --stage:#231f20;
    --orange:#f64a12;
    --orange-soft:#f7794a;
    --ink:#1c1c1c;
    --paper:#ffffff;
    --mist:#f1f1f1;
    --grey-btn:#b8b8b8;
    --caption:#cfcfcf;
  }
  *{box-sizing:border-box;margin:0;padding:0}
  html,body{width:1200px;height:1171px;overflow:hidden;background:var(--stage)}
  body{position:relative;font-family:"Quicksand",sans-serif;color:var(--ink)}
  .page{position:absolute;top:65px;width:540px;height:959px;background:var(--paper);overflow:hidden}
  .page--cover{left:35px}
  .page--intro{left:624px}
  .abs{position:absolute}

  /* cover */
  .cover-photo{position:absolute;left:0;top:0}
  .cover-brand{left:60px;top:276px;color:#fff;font-weight:500;font-size:43px;letter-spacing:-.5px;line-height:1}
  .cover-tag{left:61px;top:323px;color:#fff;font-size:16px;letter-spacing:5.4px;font-weight:500}
  .cover-title{left:63px;top:660px;font-size:22px;line-height:22.5px;font-weight:500}
  .btn-outline{border:2px solid var(--orange);color:var(--orange);font-size:6px;font-weight:700;display:flex;align-items:center;justify-content:center;letter-spacing:.2px}
  .cover-btn{left:63px;top:764px;width:87px;height:27px}
  .accent-bar{left:354px;top:668px;width:31px;height:5px;background:var(--orange)}
  .cover-copy{left:354px;top:686px;width:122px;font-size:7px;line-height:10.4px;font-weight:500}
  .link-more{color:var(--orange);font-size:6.5px;font-weight:700;display:flex;align-items:center;gap:6px}
  .cover-more{left:354px;top:767px}
  .site{display:flex;align-items:center;gap:6px;font-size:8px;letter-spacing:.6px;font-weight:600}
  .site i{width:6px;height:6px;border-radius:50%;background:var(--orange)}
  .cover-site{left:389px;top:845px}
  .cover-band{left:0;top:895px;width:540px;height:64px;background:linear-gradient(90deg,var(--orange) 0%,var(--orange-soft) 55%,rgba(246,74,18,0) 100%)}

  /* intro */
  .intro-brand{left:52px;top:40px;font-size:8px;font-weight:700}
  .btn-fill{height:17px;color:#fff;font-size:5px;font-weight:700;display:flex;align-items:center;justify-content:center}
  .btn-app{left:381px;top:31px;width:44px;background:var(--orange)}
  .btn-quote{left:438px;top:31px;width:72px;background:var(--grey-btn)}
  .hero{left:0;top:66px;width:540px;height:296px;background:linear-gradient(110deg,#3e3a37 0%,#5b5650 45%,#8d8983 78%,#b9b6b1 100%)}
  .hero-brand{left:53px;top:140px;color:#fff;font-size:19px;font-weight:500;line-height:1}
  .hero-tag{left:54px;top:161px;color:#fff;font-size:7px;letter-spacing:2.3px;font-weight:600}
  .hero-box{left:53px;top:192px;width:245px;height:64px;background:rgba(20,20,20,.55);color:#fff;font-size:16px;line-height:17.5px;padding:3px 0 0 6px;font-weight:500}
  .hero-btn{left:54px;top:284px;width:67px;height:21px;background:rgba(20,20,20,.5);color:#fff;border-color:var(--orange);font-size:4.5px}
  .mist{left:0;top:0}
  .strip{left:0;top:421px;width:30px;height:300px;background:linear-gradient(180deg,rgba(246,74,18,.15),var(--orange) 55%,rgba(246,74,18,0))}
  .section-title{left:89px;top:462px;font-size:15px}
  .section-title b,.values-title b{font-weight:700}
  .chip{display:flex;align-items:center;height:28px;background:#fff;font-size:9.5px;font-weight:500}
  .chip .ico{width:30px;height:28px;background:var(--orange);display:flex;align-items:center;justify-content:center;margin-right:13px}
  .chip-app{left:90px;top:450px;width:150px}
  .chip-web{left:285px;top:450px;width:111px}
  .chip-seo{left:90px;top:489px;width:131px}
  .chip-gfx{left:285px;top:489px;width:116px}
  .spec-more{left:83px;top:548px;font-size:8px}
  .values-art{left:53px;top:698px;width:111px;height:83px;background:radial-gradient(circle,#fbd3c2 0%,#fde9e0 70%,#fff 100%)}
  .divider{left:210px;top:637px;width:1px;height:156px;background:#d9d9d9}
  .values-title{left:245px;top:640px;font-size:13px;line-height:16px}
  .value{font-size:8px;font-weight:600}
  .value svg{display:block;margin-bottom:3px}
  .cta{left:0;top:841px;width:540px;height:71px;background:linear-gradient(90deg,var(--orange),var(--orange-soft))}
  .cta-text{left:81px;top:857px;color:#fff;font-size:11px;line-height:12px;font-weight:600}
  .cta-btn{left:370px;top:862px;width:85px;height:21px;background:#fff;color:var(--orange);font-size:5px;font-weight:700;display:flex;align-items:center;justify-content:center}
  .intro-site{left:23px;top:942px;font-size:5.5px;letter-spacing:.2px}
  .footer-rule{left:118px;top:946px;width:330px;height:1px;background:#bbb}
  .folio{left:458px;top:942px;font-size:5.5px;font-weight:600}
  .folio b{font-size:7px}

  .caption{position:absolute;left:0;width:1158px;top:1103px;text-align:center;color:var(--caption);font-family:"PT Sans",sans-serif;font-size:21px}
</style>
</head>
<body>

<section class="page page--cover">
  <svg class="cover-photo" width="540" height="562" viewBox="0 0 540 562" role="img" aria-label="Photo d'un salon d'agence avec canapés, table basse, plante et paroi ajourée">
    <defs>
      <linearGradient id="coverPhoto" x1="0" y1="0" x2="1" y2="1">
        <stop offset="0" stop-color="#6c6866"/>
        <stop offset=".5" stop-color="#57524d"/>
        <stop offset="1" stop-color="#3f4a3a"/>
      </linearGradient>
    </defs>
    <path d="M0 0H540V354C520 450 450 540 345 561H60L0 502Z" fill="url(#coverPhoto)"/>
  </svg>
  <div class="abs cover-brand">LoomHarbor</div>
  <div class="abs cover-tag">AGENCE DIGITALE</div>

  <h1 class="abs cover-title">Agence digitale,<br>Spécialiste du web<br>et des applications<br>mobiles</h1>
  <div class="abs btn-outline cover-btn">NOS SPECIALITIES</div>
  <div class="abs accent-bar"></div>
  <p class="abs cover-copy">Lorem ipsum dolor sit amet, consectetur adipiscing elit. Mauris ipsum odio, vehicula ac venenatis at, maximus in dolor. Maecenas posuere consequat lectus sed faucibus.</p>
  <div class="abs link-more cover-more">Découvrez nos solutions
    <svg width="13" height="6" viewBox="0 0 13 6"><path d="M0 3H12M9 .5 12 3 9 5.5" fill="none" stroke="currentColor" stroke-width="1"/></svg>
  </div>
  <div class="abs site cover-site"><i></i>www.loomharbor.studio</div>
  <div class="abs cover-band"></div>
</section>

<section class="page page--intro">
  <div class="abs intro-brand">Loom Harbor</div>
  <div class="abs btn-fill btn-app">L'appli resto</div>
  <div class="abs btn-fill btn-quote">DEMANDER UN DEVIS</div>

  <div class="abs hero" role="img" aria-label="Photo de l'équipe au travail dans les bureaux, écrans et paroi ajourée"></div>
  <div class="abs hero-brand">LoomHarbor</div>
  <div class="abs hero-tag">AGENCE DIGITALE</div>
  <div class="abs hero-box">Agence digitale,<br>Spécialiste du web<br>et des applications mobiles</div>
  <div class="abs btn-outline hero-btn">NOS SPECIALITIES</div>

  <svg class="abs mist" width="540" height="959" viewBox="0 0 540 959" aria-hidden="true">
    <path d="M0 360L540 372V586L0 611Z" fill="var(--mist)"/>
  </svg>
  <div class="abs strip" role="img" aria-label="Motif de triangles orange"></div>

  <h2 class="abs section-title" style="font-weight:500"><b>Nos</b> spécialités</h2>
  <div class="abs chip chip-app"><span class="ico"><svg width="14" height="14" viewBox="0 0 14 14"><path d="M7 1 12.5 4V10L7 13 1.5 10V4ZM1.5 4 7 7 12.5 4M7 7V13" fill="none" stroke="#fff" stroke-width="1"/></svg></span>Application mobile</div>
  <div class="abs chip chip-web"><span class="ico"><svg width="14" height="14" viewBox="0 0 14 14"><path d="M13 1 1 7 6 8 7 13ZM6 8 13 1" fill="none" stroke="#fff" stroke-width="1"/></svg></span>Site Web</div>
  <div class="abs chip chip-seo"><span class="ico"><svg width="14" height="14" viewBox="0 0 14 14"><circle cx="7" cy="8" r="5" fill="none" stroke="#fff"/><path d="M7 5V8H9M2 3 4 1M12 3 10 1" fill="none" stroke="#fff"/></svg></span>Redaction SEO</div>
  <div class="abs chip chip-gfx"><span class="ico"><svg width="14" height="14" viewBox="0 0 14 14"><circle cx="3" cy="4" r="2" fill="none" stroke="#fff"/><circle cx="3" cy="10" r="2" fill="none" stroke="#fff"/><path d="M5 5 13 10M5 9 13 4" fill="none" stroke="#fff"/></svg></span>Graphisme</div>
  <div class="abs link-more spec-more">Découvrez nos solutions
    <svg width="16" height="7" viewBox="0 0 16 7"><path d="M0 3.5H15M11.5 .5 15 3.5 11.5 6.5" fill="none" stroke="currentColor" stroke-width="1"/></svg>
  </div>

  <div class="abs values-art" role="img" aria-label="Illustration d'une poignée de main"></div>
  <div class="abs divider"></div>
  <h2 class="abs values-title" style="font-weight:500">Les <b>Valeurs de l'agence<br>digitale Loom Harbor</b></h2>
  <div class="abs value" style="left:248px;top:706px"><svg width="12" height="12" viewBox="0 0 12 12"><circle cx="6" cy="6" r="5" fill="none" stroke="var(--orange)"/><path d="M4 7.2Q6 9 8 7.2" fill="none" stroke="var(--orange)"/></svg>Relation Client</div>
  <div class="abs value" style="left:360px;top:706px"><svg width="12" height="12" viewBox="0 0 12 12"><path d="M3 11H9M4 11 5 5 3 3 6 1 8 3 7 5 8 11" fill="none" stroke="var(--orange)"/></svg>Innovation</div>
  <div class="abs value" style="left:248px;top:746px"><svg width="12" height="12" viewBox="0 0 12 12"><path d="M11 1 1 6 5 7 6 11ZM5 7 11 1" fill="none" stroke="var(--orange)"/></svg>Réactivité</div>
  <div class="abs value" style="left:360px;top:746px"><svg width="14" height="12" viewBox="0 0 14 12"><path d="M7 1C10.5 1 13 3 13 5.5S10.5 10 7 10L3 11.5 4 9C2 8 1 7 1 5.5 1 3 3.5 1 7 1Z" fill="none" stroke="var(--orange)"/></svg>Communication</div>
  <div class="abs link-more" style="left:381px;top:813px;font-size:8px">Découvrez nos solutions
    <svg width="16" height="7" viewBox="0 0 16 7"><path d="M0 3.5H15M11.5 .5 15 3.5 11.5 6.5" fill="none" stroke="currentColor" stroke-width="1"/></svg>
  </div>

  <div class="abs cta"></div>
  <p class="abs cta-text">Parlez nous de votre projet web et<br>nous vous apporterons l'aide dont<br>vous avez besoin</p>
  <div class="abs cta-btn">DEMANDER UN DEVIS</div>

  <div class="abs site intro-site"><i></i>www.loomharbor.studio</div>
  <div class="abs footer-rule"></div>
  <div class="abs folio">Introduction / <b>02</b></div>
</section>

<p class="caption">Pages 1 &amp; 2 of 10... More pages to follow soon.</p>

</body>
</html>
```